Flyer für Lach- und Humorworkshops
Zielgruppe
Ich biete Lach- und Humorworkshops an für Unternehmen und Privatpersonen, für mehr Lebensfreude und Erfolg, ob privat oder im Business.
Aufgabenstellung
- DIN A6
- Textvorgabe im Word kann auch gekürzt werden, je nach Platz auf dem Flyer
- Schlagwörter wie 'Lachen' in der Schrift 'Licorice' so wie auf der Website

```html
<!DOCTYPE html>
<html lang="de">
<head>
<meta charset="utf-8">
<title>Lach-Workshop Flyer</title>
<link rel="stylesheet" href="https://fonts.googleapis.com/css2?family=Licorice&family=Poppins:wght@300;400;500;600&display=swap">
<style>
  :root {
    --bg: #efe3cc;
    --page: #f6f3f1;
    --band: #ece3dc;
    --hero-tint: #efe6e3;
    --ink: #1f1a18;
    --brown: #6f605a;
    --brown-light: #8a7b74;
    --gold: #c4a06a;
    --gold-light: #e2cda4;
    --line: #cdbfb6;
  }
  * { box-sizing: border-box; margin: 0; padding: 0; }
  html, body { width: 1200px; height: 1009px; overflow: hidden; }
  body { background: var(--bg); font-family: "Poppins", sans-serif; font-weight: 300; color: var(--brown); position: relative; }

  .page { position: absolute; top: 115px; width: 489px; height: 692px; background: var(--page); overflow: hidden; box-shadow: 0 6px 18px rgba(90,70,50,.18); }
  .page--front { left: 83px; }
  .page--back { left: 608px; }
  .abs { position: absolute; }

  .script { font-family: "Licorice", cursive; font-weight: 400; }

  /* front */
  .hero { left: 0; top: 0; width: 489px; height: 265px; background: linear-gradient(90deg, #ead8d2 0%, var(--hero-tint) 55%, var(--page) 100%); }
  .hero-art { left: 0; top: 8px; width: 236px; height: 257px; background: radial-gradient(circle at 30% 35%, #c96b4e 0%, #2f6c6b 35%, #b7c9c6 62%, #e6dbd6 100%); }
  .hero-question { left: 246px; top: 30px; font-size: 20.5px; line-height: 20px; font-weight: 400; color: var(--ink); }
  .hero-word { left: 243px; top: 68px; font-size: 96px; line-height: 1; color: var(--ink); }
  .hero-stroke { left: 240px; top: 150px; }
  .hero-text { left: 246px; top: 191px; width: 225px; font-size: 11.3px; line-height: 13.9px; color: var(--brown-light); }

  .features { left: 0; top: 265px; width: 489px; height: 189px; }
  .features-brand { left: 40px; top: 10px; font-size: 110px; font-weight: 300; color: #fff; opacity: .7; letter-spacing: 2px; }
  .feature { display: flex; align-items: center; gap: 14px; font-size: 12.4px; line-height: 15.5px; color: var(--brown-light); }
  .feature svg { flex: 0 0 auto; }

  .workshop { left: 0; top: 454px; width: 489px; height: 238px; background: var(--band); }
  .workshop-photo { left: 0; top: -20px; width: 222px; height: 258px; background: linear-gradient(180deg, #b69985 0%, #8a6b5c 40%, #2b2523 75%, #3a3230 100%); }
  .workshop-title { left: 24px; top: 10px; color: var(--ink); }
  .workshop-title .script { display: block; font-size: 44px; line-height: 34px; }
  .workshop-title .plain { display: block; font-size: 18px; font-weight: 400; line-height: 22px; }
  .workshop-lead { left: 232px; top: 34px; width: 240px; font-size: 11.2px; line-height: 14.6px; font-weight: 600; color: var(--brown); }
  .workshop-text { left: 232px; top: 115px; width: 240px; font-size: 11.2px; line-height: 13.9px; color: var(--brown-light); }

  /* back */
  .business { left: 0; top: 0; width: 489px; height: 245px; background: linear-gradient(90deg, var(--page) 40%, #ece8e6 100%); }
  .business-art { left: 270px; top: 0; width: 219px; height: 245px; background: radial-gradient(circle at 60% 40%, #d6d0cd 0%, #e8e4e2 55%, rgba(246,243,241,0) 100%); }
  .business-title { left: 34px; top: 18px; font-size: 34px; line-height: 1; color: var(--gold); }
  .business-sub { left: 33px; top: 54px; font-size: 17px; font-weight: 400; color: var(--brown); }
  .business-text { left: 33px; top: 89px; width: 425px; font-size: 11.3px; line-height: 15.5px; color: var(--brown); }

  .topics { left: 0; top: 245px; width: 489px; height: 144px; background: var(--band); }
  .topics-head { left: 34px; top: 16px; width: 420px; font-size: 12.6px; line-height: 16.5px; font-weight: 600; color: var(--brown); }
  .topics-list { list-style: none; font-size: 13.2px; line-height: 19.8px; color: var(--brown); }
  .topics-list li::before { content: "• "; font-size: 10px; }

  .about { left: 0; top: 389px; width: 489px; height: 293px; }
  .about-photo { left: 0; top: 12px; width: 180px; height: 281px; background: linear-gradient(180deg, #efe6dc 0%, #c99f84 35%, #5a463d 60%, #2a2422 100%); }
  .about-label { left: 187px; top: 11px; font-size: 12.6px; color: var(--brown-light); }
  .about-name { left: 187px; top: 26px; font-size: 48px; line-height: 1; color: var(--gold); }
  .about-tagline { left: 187px; top: 80px; font-size: 12.6px; font-weight: 400; color: var(--ink); }
  .about-text { left: 187px; top: 104px; width: 270px; font-size: 11.1px; line-height: 13.8px; color: var(--brown); }
  .about-rule { left: 187px; top: 329px; }
  .divider { left: 187px; top: 207px; width: 274px; height: 1px; background: var(--line); }
  .brand-name { left: 187px; top: 228px; font-size: 38px; font-weight: 300; color: var(--gold); letter-spacing: 1px; }
  .contact { left: 340px; top: 221px; font-size: 11.8px; line-height: 15px; color: var(--brown-light); }
  .contact strong { font-weight: 600; color: var(--brown); }
  .gold-bar { left: 0; top: 682px; width: 489px; height: 10px; background: linear-gradient(90deg, var(--gold) 0%, var(--gold-light) 50%, var(--gold) 100%); }
</style>
</head>
<body>

<section class="page page--front">
  <div class="abs hero">
    <div class="abs hero-art" role="img" aria-label="Gemalte Illustration einer lachenden Frau mit Blumen im Haar"></div>
    <p class="abs hero-question">Wann hast du das<br>letzte Mal so richtig</p>
    <p class="abs hero-word script">gelacht?</p>
    <svg class="abs hero-stroke" width="240" height="40" viewBox="0 0 240 40"><path d="M40 37 C90 28 150 25 210 22" stroke="#d9c6b6" stroke-width="2" fill="none" stroke-linecap="round"/></svg>
    <p class="abs hero-text">Lachen ist nicht nur ein Ausdruck von Freude, es ist gesund für unseren Körper, ausgleichend für unseren Geist und Balsam für unsere Seele.</p>
  </div>

  <div class="abs features">
    <span class="abs features-brand">lumara</span>
    <div class="abs feature" style="left:20px; top:48px;">
      <svg width="36" height="32" viewBox="0 0 36 32" fill="none" stroke="#c8a68c" stroke-width="1.3"><path d="M18 14 C12 8 8 12 12 16 L18 22 L24 16 C28 12 24 8 18 14Z"/><path d="M4 14 C6 22 10 28 14 30 M32 14 C30 22 26 28 22 30"/></svg>
      <span>Lachen ist einfach, gesund<br>und macht glücklich.</span>
    </div>
    <div class="abs feature" style="left:264px; top:48px;">
      <svg width="28" height="28" viewBox="0 0 28 28" fill="none" stroke="#c8a68c" stroke-width="1.3"><circle cx="14" cy="14" r="11"/><circle cx="14" cy="14" r="6"/><path d="M8 14 H20 M14 8 V20"/></svg>
      <span>Lachen ist eine universelle<br>Sprache, die verbindet.</span>
    </div>
    <div class="abs feature" style="left:22px; top:113px;">
      <svg width="36" height="28" viewBox="0 0 36 28" fill="none" stroke="#c8a68c" stroke-width="1.3"><circle cx="11" cy="17" r="9"/><circle cx="25" cy="17" r="9"/><path d="M7 19 Q11 23 15 19 M21 19 Q25 23 29 19 M18 2 V6 M12 4 L14 7 M24 4 L22 7"/></svg>
      <span>Lachen ist sofort wirksam<br>und nachhaltig zugleich.</span>
    </div>
    <div class="abs feature" style="left:266px; top:113px;">
      <svg width="30" height="30" viewBox="0 0 30 30" fill="none" stroke="#c8a68c" stroke-width="1.3"><path d="M15 4 C12 8 12 12 15 15 C18 12 18 8 15 4Z M15 15 C10 14 7 10 7 7 C11 8 14 11 15 15 M15 15 C20 14 23 10 23 7 C19 8 16 11 15 15"/><path d="M3 22 C8 18 14 20 18 22 L27 18 M3 26 L10 26"/></svg>
      <span>Lachen ist ganzheitlich,<br>nachhaltig und sinnvoll.</span>
    </div>
  </div>

  <div class="abs workshop">
    <div class="abs workshop-photo" role="img" aria-label="Foto einer lachenden Trainerin im schwarzen T-Shirt"></div>
    <p class="abs workshop-title"><span class="script">Lach-</span><span class="plain">Workshop</span></p>
    <p class="abs workshop-lead">Du suchst eine besondere Teambuilding Aktivität? Wie wäre es mit einer kurzen Auszeit aus dem Alltag, die lustig, gesund, nachhaltig und sinnvoll ist?</p>
    <p class="abs workshop-text">In einem Lach-Workshop geht es in erster Linie darum, gemeinsam Spass zu haben und ausgiebig zu lachen. Euch erwartet ein abwechslungsreicher Mix aus einfachen, spielerischen und kreativen Übungen.</p>
  </div>
</section>

<section class="page page--back">
  <div class="abs business">
    <div class="abs business-art" role="img" aria-label="Blasse Illustration einer lachenden Frau mit Blumen"></div>
    <p class="abs business-title script">Humor im Business –</p>
    <p class="abs business-sub">für ein positives Betriebsklima</p>
    <p class="abs business-text">Lachen ist gesund – das gilt nicht nur für unsere persönliche Gesundheit, sondern auch für ein Unternehmen. Lachen ist eine universelle, positive Form der Kommunikation. Lachen ist essentiell für zwischenmenschliche Beziehungen, denn Lachen schafft Vertrauen und Nähe. Wo gelacht wird, fühlen wir uns wohl, der Teamgeist wird gestärkt, Kreativität und Leistungsbereitschaft werden gefördert. Gesunde, zufriedene, motivierte und ausgeglichene Mitarbeitende lösen Herausforderungen viel kreativer und effizienter. Denn nur wer Freude hat bei der Arbeit, ist zu dauerhaften Höchstleistungen fähig.</p>
  </div>

  <div class="abs topics">
    <p class="abs topics-head">Lachen &amp; Humor lässt sich sehr vielseitig integrieren, kann einen Anlass bereichern oder ergänzen:</p>
    <ul class="abs topics-list" style="left:35px; top:66px;">
      <li>Teambuilding</li>
      <li>Persönlichkeitsentwicklung</li>
      <li>Stressmanagement</li>
    </ul>
    <ul class="abs topics-list" style="left:251px; top:66px;">
      <li>Gesundheit &amp; Wohlbefinden</li>
      <li>Kreaktivität &amp; Innovation</li>
    </ul>
  </div>

  <div class="abs about">
    <div class="abs about-photo" role="img" aria-label="Porträtfoto der Lach-Trainerin"></div>
    <p class="abs about-label">Über mich:</p>
    <p class="abs about-name script">Ich bin Lina</p>
    <p class="abs about-tagline">Natürlich. Empathisch. Professionell.</p>
    <p class="abs about-text">Ich lache fürs Leben gerne! Als Lach-Trainerin habe ich es mir zur Aufgabe gemacht, Menschen mit Lachen &amp; Humor zu inspirieren. Mein persönliches Ziel ist es, mehr Vitalität und Zufriedenheit in den Alltag möglichst vieler Menschen zu bringen, mit etwas, das so einfach, natürlich und alltäglich ist: LACHEN.</p>
    <div class="abs divider"></div>
    <p class="abs brand-name">lumara</p>
    <p class="abs contact"><strong>Lina Berger</strong><br>www.lumara-lachen.ch<br>hallo@lumara-lachen.ch<br>+41 79 000 12 34</p>
  </div>
  <div class="abs gold-bar"></div>
</section>

</body>
</html>
```